High impact classy folder for an HVAC and Electrical contractor

We need a folder designed. It needs to be high impact and classy with a rich look to it. We want to cement our branding via the use of the folder so the look will need to have impact with use of our logo and colors.

We want to pull the entire brand look and feel together with this folder. We are going to be making other marketing materials and this is the start of a much larger project. In the ideal situation the winning desginer will continue on with the rest of the projects because they will know how to apply the brand look.

We want to give our local company the feel of a national franchise. Wherein the brand is very prominent and is repeated over and over again.

Use of logo and color scheme will be important.

We like dark backgrounds because they really make the logo pop.

Target Market(s)

homeowners

Font styles to use
Serif

Requirements
Must have
• Logo prominent on the front
• Our Tag Line:
• The Best Way To Live In New Jersey Is With Hearthline"
• On the inside pockets:
• Our Phone number: 973-555-0184
• A message to our customers:
• We want to thank you for choosing Hearthline Partners today
• Our name says it all, because for over 30 years we have prided ourselves on delivering the best service and exceeding our customers' expectations everyday. Whether you need something fixed, replaced or upgraded, no matter how large or small, the dedicated and experts at Hearthline Partners are here to take care of you. Delivering the right solution for you the first time- everytime - and ensuring you are always 100% satisfied. If for any reason you want to speak with us, please do not hesitate to call or email. Thank you again for choosing Hearthline Partners.
• On the rear: a graphic that says 24-7 service
• A list of other services we provide:
• Solar
• Generators
• Home Security
• Home Automation
• Home Inspection
• Energy Audits
• 1 Day Bathroom remodles
• Basement Waterproofing
• Garage Doors
• Home Theaters
Nice to have
• I added photos of a flyer and of a mobile website to give an idea of the color scheme as well

```html
<!DOCTYPE html>
<html lang="en">
<head>
<meta charset="utf-8">
<title>Hearthline Partners – Presentation Folder</title>
<link href="https://fonts.googleapis.com/css2?family=Cinzel:wght@400;700&family=Open+Sans:wght@400;600;700&display=swap" rel="stylesheet">
<style>
  :root {
    --stage: #e9cfd0;
    --brand-red: #8f1820;
    --brand-red-dark: #6f0f16;
    --brand-orange: #e07a1f;
    --brand-gold: #f29a2e;
    --cream: #f5e6c8;
    --paper: #ffffff;
    --paper-grey: #dcdcdc;
    --silver: #c9c9c9;
    --card-black: #2a2a2a;
  }
  * { box-sizing: border-box; margin: 0; padding: 0; }
  html, body { width: 1200px; height: 847px; overflow: hidden; }
  body {
    background: radial-gradient(ellipse at 40% 40%, #f4e4e4 0%, var(--stage) 60%, #d7a7a9 100%);
    font-family: "Open Sans", Arial, sans-serif;
    position: relative;
  }

  /* ---------- Front cover ---------- */
  .front-cover {
    position: absolute; left: 70px; top: 150px;
    width: 330px; height: 540px;
    background: linear-gradient(180deg, var(--brand-red) 0%, var(--brand-red-dark) 100%);
    overflow: hidden;
    box-shadow: 0 18px 40px rgba(90, 30, 30, .25);
  }
  .cover-photo {
    position: absolute; left: 0; top: 0; width: 330px; height: 230px;
    background: linear-gradient(180deg, #e8e8e8 0%, #c9ccd4 45%, #8a7a6a 100%);
    clip-path: path("M0 0 H330 V170 Q160 142 0 205 Z");
  }
  .cover-swoosh { position: absolute; left: 0; top: 0; width: 330px; height: 240px; }
  .cover-name {
    position: absolute; left: 0; right: 0; top: 268px;
    text-align: center;
    font-family: "Cinzel", Georgia, serif; font-weight: 700;
    color: var(--cream);
    font-size: 38px; line-height: 1.05; letter-spacing: 1px;
  }
  .tagline-band {
    position: absolute; left: 0; right: 0; top: 462px; height: 30px;
    background: linear-gradient(180deg, #f2f2f2 0%, var(--silver) 100%);
    display: flex; align-items: center; justify-content: center;
    padding: 0 8px;
  }
  .tagline {
    font-family: "Cinzel", Georgia, serif; font-size: 9.4px;
    color: var(--brand-red); letter-spacing: 0; white-space: nowrap;
  }
  .cover-rule { position: absolute; left: 0; right: 0; height: 2px; }
  .cover-rule.silver { top: 512px; background: var(--silver); }
  .cover-rule.orange { top: 518px; background: var(--brand-orange); }

  /* ---------- Inside spread ---------- */
  .inside-spread {
    position: absolute; left: 470px; top: 150px;
    width: 660px; height: 540px;
    display: flex;
    box-shadow: 0 18px 40px rgba(90, 30, 30, .25);
  }
  .inside-panel { position: relative; width: 50%; height: 100%; }
  .inside-panel.left { background: linear-gradient(120deg, var(--paper) 55%, #e6e6e6 100%); }
  .inside-panel.right { background: linear-gradient(90deg, #cfcfcf 0%, var(--paper-grey) 30%, #e4e4e4 100%); }
  .pocket {
    position: absolute; left: 0; right: 0; bottom: 0; height: 200px;
    background: var(--brand-red);
  }
  .inside-panel.left .pocket { border-right: 1px solid var(--brand-red-dark); }
  .pocket-message { position: absolute; left: 28px; right: 22px; top: 22px; }
  .message-title { color: var(--brand-gold); font-weight: 700; font-size: 9px; margin-bottom: 6px; }
  .message-body { color: #fff; font-size: 6.6px; line-height: 1.75; }
  .call-line {
    position: absolute; left: 28px; bottom: 28px;
    font-weight: 700; font-size: 25px; color: #fff; white-space: nowrap;
  }
  .call-line .phone { color: var(--brand-gold); }

  .card-slot { position: absolute; left: 82px; top: 36px; width: 150px; height: 92px; }
  .business-card {
    position: absolute; inset: 0;
    background: var(--card-black);
    box-shadow: 2px 3px 0 #111;
    display: flex; align-items: center; justify-content: center;
  }
  .business-card::before, .business-card::after {
    content: ""; position: absolute; left: 0; right: 0; height: 3px; background: var(--brand-orange);
  }
  .business-card::before { top: 9px; }
  .business-card::after { bottom: 9px; }
  .card-name { color: #fff; font-weight: 600; font-size: 11.5px; }
</style>
</head>
<body>

  <section class="front-cover">
    <div class="cover-photo" role="img" aria-label="Photo of a team of contractors in hard hats with a tool belt in the foreground"></div>
    <svg class="cover-swoosh" viewBox="0 0 330 240" aria-hidden="true">
      <path d="M0 205 Q160 142 330 170" fill="none" stroke="#e07a1f" stroke-width="9"/>
      <path d="M0 216 Q160 156 330 184" fill="none" stroke="#d3d3d3" stroke-width="10"/>
      <path d="M0 226 Q160 170 330 196" fill="none" stroke="#f3f3f3" stroke-width="5"/>
    </svg>
    <h1 class="cover-name">Hearthline<br>Partners</h1>
    <div class="tagline-band">
      <p class="tagline">The Best Way To Live In New Jersey Is With Hearthline"</p>
    </div>
    <div class="cover-rule silver"></div>
    <div class="cover-rule orange"></div>
  </section>

  <section class="inside-spread">
    <div class="inside-panel left">
      <div class="pocket">
        <div class="pocket-message">
          <h2 class="message-title">We want to thank you for choosing Hearthline Partners today</h2>
          <p class="message-body">Our name says it all, because for over 30 years we have prided ourselves on delivering the best service and exceeding our customers' expectations everyday. Whether you need something fixed, replaced or upgraded, no matter how large or small, the dedicated and experts at Hearthline Partners are here to take care of you. Delivering the right solution for you the first time- everytime - and ensuring you are always 100% satisfied. If for any reason you want to speak with us, please do not hesitate to call or email. Thank you again for choosing Hearthline Partners.</p>
        </div>
        <p class="call-line">Call Us <span class="phone">973-555-0184</span></p>
      </div>
    </div>
    <div class="inside-panel right">
      <div class="pocket">
        <div class="card-slot">
          <div class="business-card"><span class="card-name">Pocketline Print</span></div>
        </div>
      </div>
    </div>
  </section>

</body>
</html>
```